CareVantRx business cards

We need a business card design that we could customize as needed for employees. We will need space for Name, Title, 1-2 phone numbers and email address.

We are a Pharmacy Benefits Management (PBM) company for hospice agencies and beginning a nationwide expansion. Attached is a vector file of our logo.

Cards can be single or double sided.

Industry/Entity Type

Business

```html
<!DOCTYPE html>
<html lang="en">
<head>
<meta charset="UTF-8">
<title>CareVantRx Business Cards</title>
<link rel="stylesheet" href="https://fonts.googleapis.com/css2?family=Questrial&display=swap">
<style>
  :root {
    --canvas: #2b2b2b;
    --card: #ffffff;
    --card-shade: #f1f1f1;
    --brand-green: #7f9a45;
    --brand-green-light: #a3b86c;
    --brand-blue: #1f5f8b;
    --ink: #2f2f2f;
    --ink-soft: #555555;
    --wash: #dfe6ea;
  }
  * { margin: 0; padding: 0; box-sizing: border-box; }
  html, body {
    width: 1200px;
    height: 900px;
    overflow: hidden;
    background: var(--canvas);
    font-family: "Questrial", "Century Gothic", sans-serif;
  }
  .sheet {
    position: relative;
    width: 1200px;
    height: 900px;
  }
  .card {
    position: absolute;
    left: 290px;
    width: 620px;
    height: 354px;
    background: linear-gradient(135deg, var(--card) 55%, var(--card-shade));
    overflow: hidden;
  }
  .card--back { top: 50px; }
  .card--front { top: 496px; }

  .card__bands {
    position: absolute;
    left: 0;
    bottom: 0;
    width: 620px;
    height: 40px;
  }

  /* Brand lockup */
  .brand {
    position: absolute;
    display: flex;
    align-items: center;
    gap: 14px;
  }
  .brand__square {
    background: var(--brand-green);
    border-radius: 6px;
  }
  .brand__name {
    color: var(--brand-green);
    font-weight: 400;
    letter-spacing: -0.5px;
    line-height: 1;
  }
  .card--back .brand { left: 92px; top: 118px; }
  .card--back .brand__square { width: 58px; height: 58px; }
  .card--back .brand__name { font-size: 64px; }

  .tagline {
    position: absolute;
    left: 170px;
    top: 210px;
    font-size: 15px;
    letter-spacing: 4px;
    color: var(--ink-soft);
  }

  .card--front .brand { left: 178px; top: 46px; }
  .card--front .brand__square { width: 44px; height: 44px; }
  .card--front .brand__name { font-size: 48px; }

  /* Faint corner decoration */
  .card__wash {
    position: absolute;
    background: var(--wash);
    opacity: 0.7;
    border-radius: 10px;
  }
  .card--back .card__wash { right: 26px; top: 56px; width: 110px; height: 110px; }
  .card--front .card__wash { right: 30px; top: 130px; width: 120px; height: 120px; }

  /* Person */
  .person {
    position: absolute;
    right: 40px;
    top: 112px;
    text-align: right;
  }
  .person__name {
    font-size: 24px;
    color: var(--brand-green);
    letter-spacing: 0.5px;
    font-weight: 400;
  }
  .person__title {
    font-size: 12px;
    color: var(--ink);
    letter-spacing: 0.5px;
    margin-top: 2px;
  }

  /* Contact column */
  .contact-tab {
    position: absolute;
    left: 0;
    top: 148px;
    width: 52px;
    height: 168px;
    background: var(--brand-green-light);
    border-radius: 0 10px 10px 0;
    display: flex;
    flex-direction: column;
    justify-content: space-around;
    align-items: center;
    padding: 8px 0;
  }
  .contact-tab svg { width: 24px; height: 24px; }

  .contact-list {
    position: absolute;
    left: 80px;
    top: 160px;
    list-style: none;
    font-size: 17px;
    color: var(--ink);
    line-height: 1.2;
  }
  .contact-list li { margin-bottom: 14px; }
  .contact-list .address { margin-bottom: 0; }
</style>
</head>
<body>
<main class="sheet">

  <!-- Back of card -->
  <section class="card card--back" aria-label="Business card, back">
    <div class="card__wash"></div>
    <div class="brand">
      <span class="brand__square"></span>
      <span class="brand__name">CareVantRx</span>
    </div>
    <p class="tagline">PHARMACY BENEFITS MANAGEMENT</p>
    <svg class="card__bands" viewBox="0 0 620 40" preserveAspectRatio="none" aria-hidden="true">
      <path d="M0 30 L400 30 Q420 30 430 22 L620 22 L620 40 L0 40 Z" fill="var(--brand-green-light)"/>
      <path d="M410 40 Q425 14 455 12 L620 6 L620 40 Z" fill="var(--brand-blue)"/>
      <path d="M0 36 L620 36" stroke="#ffffff" stroke-width="1" opacity="0.6"/>
    </svg>
  </section>

  <!-- Front of card -->
  <section class="card card--front" aria-label="Business card, front">
    <div class="card__wash"></div>
    <div class="brand">
      <span class="brand__square"></span>
      <span class="brand__name">CareVantRx</span>
    </div>

    <div class="person">
      <p class="person__name">YOUR NAME</p>
      <p class="person__title">DESIGNATION</p>
    </div>

    <div class="contact-tab" aria-hidden="true">
      <svg viewBox="0 0 24 24"><path d="M3 9 Q12 3 21 9 L19 12 L15 10 L15 8 Q12 7 9 8 L9 10 L5 12 Z" fill="#fff"/><rect x="6" y="13" width="12" height="7" rx="1.5" fill="#fff"/></svg>
      <svg viewBox="0 0 24 24"><rect x="7" y="3" width="10" height="7" fill="none" stroke="#fff" stroke-width="1.8"/><rect x="3" y="10" width="18" height="8" rx="1.5" fill="#fff"/><rect x="7" y="15" width="10" height="6" fill="#fff" stroke="var(--brand-green-light)" stroke-width="1.2"/></svg>
      <svg viewBox="0 0 24 24"><rect x="3" y="6" width="18" height="12" rx="1" fill="#fff"/><path d="M3 6 L12 13 L21 6" fill="none" stroke="var(--brand-green-light)" stroke-width="1.6"/></svg>
      <svg viewBox="0 0 24 24"><path d="M12 22 C7 15 5 12 5 9 A7 7 0 0 1 19 9 C19 12 17 15 12 22 Z" fill="#fff"/><circle cx="12" cy="9" r="2.6" fill="var(--brand-green-light)"/></svg>
    </div>

    <ul class="contact-list">
      <li>07 4910 2236</li>
      <li>07 4910 5874</li>
      <li>info@carevantrx.com</li>
      <li class="address">Your Complete<br>Address Details Here</li>
    </ul>

    <svg class="card__bands" viewBox="0 0 620 40" preserveAspectRatio="none" aria-hidden="true">
      <path d="M0 30 L400 30 Q420 30 430 22 L620 22 L620 40 L0 40 Z" fill="var(--brand-green-light)"/>
      <path d="M410 40 Q425 14 455 12 L620 6 L620 40 Z" fill="var(--brand-blue)"/>
      <path d="M0 36 L620 36" stroke="#ffffff" stroke-width="1" opacity="0.6"/>
    </svg>
  </section>

</main>
</body>
</html>
```